Heron Landing Post Card

I am a real estate agent with Marlowe and Partners. I would like to have two post cards designed. A Just Listed and a Just Sold post card for the bay front community of Heron Landing. Heron Landing is a residential community located on the Gulf coast of Florida. It is bordered by Osprey Sound on one side of the road and Pelican Reef Golf Course on the other side of the road. I am uploading several images that can be used on the design of the postcard as well as an example of what I would like to be included on the back. They will be oversized postcards and color on both sides.

Industry/Entity Type

Real Estate

```html
<!DOCTYPE html>
<html lang="en">
<head>
<meta charset="utf-8">
<title>Heron Landing – Just Listed Postcard</title>
<link href="https://fonts.googleapis.com/css2?family=Cinzel:wght@400;700&family=Italianno&display=swap" rel="stylesheet">
<style>
  :root{
    --sky:#a9b7db;
    --ink:#0c0c0c;
    --black:#000;
    --white:#fff;
    --paper:#ffffff;
    --zone:#f7bcc4;
    --grey-light:#e6e6e6;
    --grey-mid:#9a9a9a;
    --grey-dark:#5d5d5d;
  }
  *{box-sizing:border-box;margin:0;padding:0}
  html,body{width:870px;height:1200px;overflow:hidden;background:var(--paper)}
  body{position:relative;font-family:"Cinzel",serif;color:var(--ink)}

  /* ---------- front ---------- */
  .card-front{position:absolute;left:0;top:0;width:870px;height:567px;background:var(--sky);overflow:hidden}
  .front-shapes{position:absolute;inset:0}
  .front-title{position:absolute;left:22px;top:22px;font-family:"Cinzel",serif;font-weight:400;font-size:38px;line-height:44px;color:var(--ink);letter-spacing:1px}
  .brand{position:absolute;display:flex;align-items:center;gap:8px;font-family:"Cinzel",serif;font-weight:700;color:var(--ink)}
  .brand-mark{width:14px;height:14px;background:var(--ink);flex:none}
  .front-brand{left:22px;top:200px;font-size:17px;line-height:20px;width:180px}
  .front-blurb{position:absolute;left:20px;top:332px;width:180px;font-family:"Cinzel",serif;font-size:15.5px;line-height:19px;color:var(--sky);letter-spacing:.5px;text-transform:uppercase}
  .photo{position:absolute}

  /* ---------- back ---------- */
  .card-back{position:absolute;left:0;top:634px;width:870px;height:566px;background:var(--paper)}
  .back-photo{position:absolute;left:0;top:0;width:575px;height:494px;
    background:radial-gradient(ellipse at 50% 55%,var(--grey-mid) 0%,var(--grey-dark) 55%,var(--grey-light) 100%);
    -webkit-mask:radial-gradient(ellipse 70% 75% at 50% 50%,#000 70%,transparent 100%);
            mask:radial-gradient(ellipse 70% 75% at 50% 50%,#000 70%,transparent 100%)}
  .back-brand{left:60px;top:34px;font-size:16px;line-height:19px;width:160px}
  .agent{position:absolute;left:240px;top:22px;font-family:"Cinzel",serif;font-style:normal;font-size:24px;line-height:29px;color:var(--ink)}
  .headline{position:absolute;left:100px;top:132px;font-family:"Italianno",cursive;font-weight:400;font-size:94px;line-height:76px;color:var(--ink);white-space:nowrap}
  .rule{position:absolute;height:1px;background:var(--ink)}
  .community{position:absolute;left:0;width:575px;top:255px;text-align:center;font-size:25px;letter-spacing:1px}
  .price-date{position:absolute;top:330px;font-size:15px}
  .invite{position:absolute;left:0;width:575px;top:364px;text-align:center;font-size:15.5px;line-height:21px}
  .phone{position:absolute;left:0;width:575px;top:420px;text-align:center;font-family:"Cinzel",serif;font-size:31px;letter-spacing:1px}
  .email{position:absolute;left:0;width:575px;top:462px;text-align:center;font-size:14px}
  .badge{position:absolute;top:510px;background:var(--ink)}
  .badge-housing{left:38px;width:34px;height:30px}
  .badge-listing{left:92px;width:58px;height:24px;top:514px;border:3px solid var(--ink);background:var(--white)}

  .zone{position:absolute;background:var(--zone);font-family:Arial,Helvetica,sans-serif;color:#333}
  .zone-postage{left:731px;top:19px;width:126px;height:124px;font-size:14px;text-align:center;padding-top:40px;line-height:18px}
  .zone-address{left:581px;top:251px;width:276px;height:244px;padding:36px 22px 0 28px}
  .zone-address h3{font-weight:400;font-size:15px;text-align:center;margin-bottom:30px}
  .zone-address p{font-size:11.5px;line-height:14px}
  .zone-barcode{left:378px;top:494px;width:479px;height:62px;font-size:15px;text-align:center;padding-top:22px}
</style>
</head>
<body>

<section class="card-front" aria-label="Postcard front">
  <svg class="front-shapes" width="870" height="567" viewBox="0 0 870 567" aria-hidden="true">
    <path d="M0 287 H870 V567 H0 Z" fill="var(--black)"/>
    <path d="M262 0 C230 70 212 160 222 287 L870 287 V0 Z" fill="var(--black)"/>
  </svg>

  <div class="photo" role="img" aria-label="Waterfront homes of Heron Landing behind a green lawn and pond under blue sky"
       style="left:230px;top:0;width:640px;height:287px;background:linear-gradient(180deg,#7da6d8 0%,#bcd0e6 35%,#e6eaee 48%,#4d6b3a 62%,#6f8f4a 78%,#5f8f3c 100%);clip-path:path('M32 0 C12 70 -2 160 6 287 L640 287 L640 0 Z')"></div>

  <div class="photo" role="img" aria-label="Wooden dock reaching into Osprey Sound under a blue sky"
       style="left:207px;top:298px;width:311px;height:269px;background:linear-gradient(180deg,#3f7fd0 0%,#9cc3ea 40%,#5e86a8 58%,#2f5f86 75%,#4a3a2c 100%)"></div>

  <div class="photo" role="img" aria-label="Gated entrance with flagpole and palm trees"
       style="left:528px;top:298px;width:310px;height:269px;background:linear-gradient(180deg,#2f6ed4 0%,#7fb0e8 40%,#3f6a34 65%,#6c7a5a 85%,#8e8a80 100%);clip-path:path('M0 0 H300 C312 90 312 180 300 269 H0 Z')"></div>

  <h1 class="front-title">Heron<br>Landing</h1>
  <div class="brand front-brand"><span class="brand-mark"></span><span>Marlowe and Partners</span></div>
  <p class="front-blurb">A one of kind, upscale gated community located on Cape Willow Peninsula and nestled between the Pelican Reef Golf Course and Osprey Sound.</p>
</section>

<section class="card-back" aria-label="Postcard back">
  <div class="back-photo" role="img" aria-label="Aerial view of the Heron Landing coastline and waterways in grey tones"></div>

  <div class="brand back-brand"><span class="brand-mark"></span><span>Marlowe and Partners</span></div>
  <address class="agent">Clara Whitfield<br>4120 Bayview Road<br>Sandpoint, FL 33900</address>
  <h2 class="headline">Just Listed</h2>

  <div class="rule" style="left:52px;top:248px;width:460px"></div>
  <p class="community">In Heron Landing</p>

  <p class="price-date" style="left:44px">at $</p>
  <div class="rule" style="left:80px;top:346px;width:180px"></div>
  <p class="price-date" style="left:282px">On</p>
  <div class="rule" style="left:318px;top:346px;width:190px"></div>

  <p class="invite">Please contact me if you are interested<br>in buying or selling property in the area.</p>
  <p class="phone">555-014-2287</p>
  <p class="email">clarawhitfield@example.com</p>

  <div class="badge badge-housing" role="img" aria-label="Housing badge"></div>
  <div class="badge badge-listing" role="img" aria-label="Listing service badge"></div>

  <div class="zone zone-postage">Postage<br>Area</div>
  <div class="zone zone-address">
    <h3>Address Area</h3>
    <p>The only text allowed in the Address Area is the recipient mailing address. Red zones may have no text or graphics darker than 7% grayscale.</p>
  </div>
  <div class="zone zone-barcode">Barcode Area</div>
</section>

</body>
</html>
```